dorwial business card design so that it looks better

need a new business card designed. use our website, dorwian.com for example. I attached an example of a previous card we had and liked. this is for law enforcement and we have attached a previous business card as an example. This site forces me to select color and font, ignore those as I picked stuff just to get this completed.

Target Market(s)

law enforcement, local government

Contact Information for Business Card

see the attached example and our website

Font styles to use
Serif

```html
<!DOCTYPE html>
<html lang="en">
<head>
<meta charset="utf-8">
<title>Dorwial Business Card</title>
<link rel="stylesheet" href="https://fonts.googleapis.com/css2?family=Exo+2:wght@500&family=Roboto:ital,wght@0,300;0,400;1,400&display=swap">
<style>
  :root {
    --backdrop: #d6d6d6;
    --card: #f4f4f4;
    --ink: #1b1f24;
    --brand-blue: #1677c4;
    --band-blue: #1a6aa8;
    --band-dark: #0d1820;
    --muted-light: #d8dde2;
  }
  html, body {
    margin: 0;
    padding: 0;
    width: 1200px;
    height: 576px;
    overflow: hidden;
    background: var(--backdrop);
  }
  .canvas {
    position: relative;
    width: 1200px;
    height: 576px;
    font-family: "Roboto", Arial, sans-serif;
    color: var(--ink);
  }
  .card {
    position: absolute;
    top: 138px;
    width: 484px;
    height: 294px;
    background: var(--card);
    border-radius: 12px;
    overflow: hidden;
  }
  .card--front { left: 82px; }
  .card--back { left: 602px; }

  .wordmark {
    position: absolute;
    margin: 0;
    font-family: "Roboto", Arial, sans-serif;
    font-weight: 300;
    color: var(--ink);
    letter-spacing: 0.06em;
    line-height: 1;
    white-space: nowrap;
  }
  .card--front .wordmark {
    left: 0;
    right: 0;
    top: 126px;
    text-align: center;
    font-size: 60px;
  }
  .card--back .wordmark {
    left: 34px;
    top: 122px;
    font-size: 46px;
  }

  .bands {
    position: absolute;
    left: 0;
    bottom: 0;
    width: 484px;
    height: 40px;
  }
  .band--blue { fill: var(--band-blue); }
  .band--dark { fill: var(--band-dark); }

  .front-url {
    position: absolute;
    left: 296px;
    bottom: 9px;
    width: 150px;
    font-size: 12.5px;
    font-weight: 300;
    letter-spacing: 0.28em;
    color: var(--muted-light);
    white-space: nowrap;
  }

  .contact {
    position: absolute;
    left: 292px;
    top: 66px;
  }
  .contact__name {
    margin: 0;
    font-family: "Exo 2", "Roboto", sans-serif;
    font-weight: 500;
    font-size: 21px;
    line-height: 1;
    color: var(--brand-blue);
  }
  .contact__title {
    margin: 4px 0 0;
    font-style: italic;
    font-size: 12.5px;
    color: #2b3138;
  }
  .contact__address {
    margin: 14px 0 0;
    font-style: normal;
    font-size: 12.5px;
    line-height: 16px;
    color: #2b3138;
  }
  .contact__lines {
    list-style: none;
    margin: 8px 0 0;
    padding: 0;
    font-size: 12.5px;
    line-height: 17px;
    color: #2b3138;
  }
  .contact__lines li {
    display: flex;
    align-items: center;
  }
  .contact__icon {
    width: 10px;
    height: 10px;
    margin: 0 11px 0 6px;
    fill: var(--band-blue);
    flex: none;
  }
  .tagline {
    position: absolute;
    left: 250px;
    bottom: 10px;
    margin: 0;
    font-size: 12.5px;
    color: #2b3138;
    white-space: nowrap;
  }
  .tagline__divider { margin: 0 9px; }
</style>
</head>
<body>
<main class="canvas">

  <section class="card card--front" aria-label="Card front">
    <p class="wordmark">DORWIAL</p>
    <svg class="bands" viewBox="0 0 484 40" aria-hidden="true">
      <polygon class="band--blue" points="0,16 193,16 183,40 0,40"/>
      <polygon class="band--blue" points="200,16 264,16 254,40 190,40"/>
      <polygon class="band--dark" points="284,2 484,2 484,40 262,40"/>
    </svg>
    <span class="front-url">www.dorwian.com</span>
  </section>

  <section class="card card--back" aria-label="Card back">
    <p class="wordmark">DORWIAL</p>

    <div class="contact">
      <h1 class="contact__name">Martin Kessler</h1>
      <p class="contact__title">Founder/Chief Exe. Officer</p>
      <address class="contact__address">4218 Larkspur Avenue<br>Austin, TX 78704</address>
      <ul class="contact__lines">
        <li>
          <svg class="contact__icon" viewBox="0 0 10 10" aria-hidden="true">
            <path d="M0.5 3.2C0.5 1.6 2.5 0.8 5 0.8s4.5 0.8 4.5 2.4L7.6 3.6 7.4 2.6H2.6L2.4 3.6Z"/>
            <rect x="1.6" y="4.4" width="6.8" height="4.8" rx="0.6"/>
          </svg>555.210.4937
        </li>
        <li>
          <svg class="contact__icon" viewBox="0 0 10 10" aria-hidden="true">
            <path d="M0.5 2h9v6h-9z M1.2 2.6 5 5.6 8.8 2.6" fill="none" stroke="var(--band-blue)" stroke-width="1.1"/>
          </svg>info@dorwian.com
        </li>
        <li>
          <svg class="contact__icon" viewBox="0 0 10 10" aria-hidden="true">
            <g fill="none" stroke="var(--band-blue)" stroke-width="0.9">
              <circle cx="5" cy="5" r="4.2"/>
              <ellipse cx="5" cy="5" rx="1.8" ry="4.2"/>
              <path d="M0.8 5h8.4"/>
            </g>
          </svg>www.dorwian.com
        </li>
      </ul>
    </div>

    <svg class="bands" viewBox="0 0 484 40" aria-hidden="true">
      <polygon class="band--blue" points="0,16 143,16 133,40 0,40"/>
      <polygon class="band--dark" points="152,16 220,16 210,40 142,40"/>
    </svg>
    <p class="tagline">Better Technology<span class="tagline__divider">|</span>Better Service</p>
  </section>

</main>
</body>
</html>
```